Major Australian Food and Wine Event Web Design Project

The project will consist of 3 designs
The homepage
A city hub page
A general content page

The main audience who will visit the website will be (in Order of importance:

1) Visitors
- Mainly women 24 – 54 years (they are the main ticket buyers)
- In a relationship – so will go to the show with their partner
- In a good paying job or home maker – and who have disposable income to spend $30 a ticker
- Enjoy food, wine and going out
- Looking for a fun day out – although an event that is about food and wine – it is an event that most people will go to and have a fun day out – not too pretentious

A smaller proportion of the audience will be:
2) Exhibitors & sponsors ( both prospective and existing)
3) Media

Objectives:

- Functionality on home page and sub pages needs to be updated, clear, easy to navigate and inject a sense of ‘fun’ – need to make it look more professional
- Need to incorporate the many things that need to be on the home page and sub pages in a visually appealing manner
- Ensure the ‘Cons’ above are considered and reflected in functionality and design
- To not be too focus on the colours (these can be changed) – but focus on the functionality and overall design opportunities.

Approach:

Keywords to describe the Bright Plate & Vine Fair:
Fun day out, discover, learn, indulge, entertaining

Other website examples:

Some great consumers event websites from the UK really make our website look basic and juvenile – and below are some examples of the presentation of how we would like our website to look like:

http://www.morselfairs-example.com/london/ This website is clean, includes good social media integration and exudes a sense of fun. Their content pages, such as the features landing page also presents options in a clear and visually appealing way with a series of boxes including image and text http://www.morselfairs-example.com/london/content/343/Features

http://www.homecraftexpo-example.com/ - this is also a great website – and it incorporates all the elements we would be looking for on our homepage – but the background/skin also includes a sense of fun and cheekiness. Subpages also are consistent.

Features

• Its a fun day that offers great value for money
• Caters to all visitors, regardless of different levels of knowledge or interest in food, wine and cooking.
• Sample great quality food and wine products from hundreds of reputable exhibitors
• Learn more through many of the shows feature activities (Celeb Theatre, Wine Theatre, Cooking & Cheese Classes)

Functionality & Structure:

In a user friendly, easy to view way, we need to incorporate the following functionality elements on home page:
- main header (that will incorporate our current creative) with a ‘fun’ skin
- navigation tabs/references (hone, location, tickets, blog, sign up, exhibitors)
- navigation/content banner (rotating)
- Area for small intro about the show
- News and highlight section
- New exhibitors section
- Obvious Ticket call to action
- Obvious sign up call to action
- Social media buttons or links ( really like the moving gifs on the Homecraftexpo-example.com site
- area for advertising (MREC size) to sell to exhibitors/sponsors
- Show dates for all 5 shows (maybe in main header)

Subpage layout is also important and needs to reflect the homepage – so would also like to see examples of how this would look and tie in with navigation – we generally have a lot of content on these pages, so clear navigation would be useful. – see below for further details of functionality for city Hubs

‘CITY HUB’ BRIEF
When navigating to each location the user will be taken to a ‘CITY HUB’ which should replicate design and content elements of a main HOME page, as well as reflect more specific information for each Show. Elements which must appear on this page are:
• FEATURES – which may be displayed in categories (in boxes, see appendix 1.0) which will link through to relevant content pages. Or in one box which will link through to a features page with all presented in boxes
• CHEFS – may be displayed as a separate icon box which will link to chefs page with bios, Celeb Theatre timetable etc.
• TICKETS – either a button or clear callout to purchase tickets
• PLAN YOUR DAY – may be displayed in a separate content box which will then link through to getting there, sample itineraries and downloadable pocket show guide for visitors to print before coming to the Show.
• WHO’S EXHIBITING – to link back to city specific exhibitor lists

Our current website is out of date and has the following inadequacies (www.brightplatefair-example.com.au) -

The homepage
A city hub page
A general content page

1) Visitors

3) Media

Objectives:

Approach:

To be perceived as a fun, entertaining event with something for everyone - website creative and navigation must reflect this.

Other website examples:

Features

- New exhibitors section

‘CITY HUB’ BRIEF

- Dated design/layout
- Homepage too text heavy
- No content boxes that can be used for different features/areas (eg. News, Exhibitors etc)
- Uninspiring colours and skin(eg. grey background), does not reflect ‘a fun day out’
- Limited presence of social media platforms and lacks ‘community’
- No continuity in sub pages
- main banner too big – takes up too much space on homepage

Requirements
Must have
• As per above brief.

In addition:
Floating social media buttons on side
Wrap around image
Drop down menu (specifically for the location nav item)

```html
<!DOCTYPE html>
<html lang="en">
<head>
<meta charset="utf-8">
<title>Bright Plate &amp; Vine Fair 2012</title>
<link rel="stylesheet" href="https://fonts.googleapis.com/css2?family=Questrial&family=Arimo:wght@400;700&display=swap">
<style>
:root{
  --red:#c21f2f;
  --red-dark:#a8162a;
  --pink:#e2177d;
  --pink-soft:#f06aa8;
  --blue:#3c8fd4;
  --blue-dark:#1f6fb5;
  --sky:#8fd0f2;
  --ink:#222;
  --grey:#555;
  --white:#fff;
  --black:#0a0a0a;
}
*{box-sizing:border-box;margin:0;padding:0}
html,body{width:1100px;height:1200px;overflow:hidden;background:#fff}
body{font-family:"Arimo",Arial,sans-serif;color:var(--ink)}
.canvas{position:relative;width:1100px;height:1200px;overflow:hidden}
.abs{position:absolute}

/* skin */
.skin{position:absolute;inset:0;background:
  radial-gradient(ellipse 260px 200px at 160px 700px,rgba(245,170,30,.75),transparent 70%),
  radial-gradient(ellipse 260px 220px at 960px 720px,rgba(245,170,30,.75),transparent 70%),
  radial-gradient(ellipse 200px 300px at 120px 300px,rgba(40,110,200,.55),transparent 70%),
  radial-gradient(ellipse 200px 300px at 980px 320px,rgba(40,110,200,.55),transparent 70%),
  linear-gradient(180deg,#a9dcf5 0%,#7cc6ee 45%,#9fd6f2 80%,#5c9a3a 97%,#2f5e20 100%)}
.skin-piece{position:absolute;border-radius:6px}
.skin-wine{left:0;top:0;width:190px;height:150px;background:linear-gradient(135deg,#4a5a2a,#d9d27a 70%,rgba(255,255,255,0));border-radius:0 0 60px 0;opacity:.85}
.skin-board{left:0;top:668px;width:245px;height:150px;background:linear-gradient(160deg,#c98b52,#8f5a2e);border-radius:0 30px 30px 0}
.skin-spoons{left:0;top:492px;width:112px;height:90px;background:linear-gradient(135deg,#d89a3a,#b8332a);border-radius:0 40px 40px 0;opacity:.8}
.skin-veg{left:822px;top:78px;width:110px;height:150px;background:linear-gradient(160deg,#e0402a,#f2a21e 60%,#8cc04a);border-radius:40px}
.skin-balloon{left:1025px;top:12px;width:40px;height:48px;background:#e54a96;border-radius:50%}

/* page panel */
.page{position:absolute;left:268px;top:15px;width:552px;height:1155px;background:var(--white);box-shadow:0 0 14px rgba(0,0,0,.35)}

.dates{left:424px;top:26px;font-size:8.5px;color:var(--pink);line-height:15px;font-family:"Questrial",sans-serif;white-space:nowrap}
.dates b{font-weight:400;margin-right:10px}
.dates-rule{left:420px;top:38px;width:400px;height:2px;background:var(--pink)}

.nav{left:263px;top:57px;width:560px;height:21px;background:var(--red);box-shadow:0 2px 3px rgba(0,0,0,.3)}
.nav ul{list-style:none;display:flex;position:absolute;left:172px;top:2px;white-space:nowrap}
.nav li{font-family:"Questrial",sans-serif;color:var(--white);font-size:13px;line-height:16px;margin-right:19px;white-space:nowrap}
.pot{left:318px;top:45px;width:64px;height:60px;background:radial-gradient(ellipse at 50% 60%,#e22c2c,#a40f16);border-radius:10px 10px 24px 24px}

.brand{left:290px;top:120px;width:120px;text-align:center;font-family:"Questrial",sans-serif;font-size:17px;line-height:20px;color:#2a2a2a}
.brand-dot{display:block;width:14px;height:14px;border-radius:50%;background:var(--red);margin:0 auto 4px}

.cta-oval{border-radius:50%;background:var(--pink);display:flex;align-items:center;justify-content:center}
.cta-oval .inner{border-radius:50%;background:var(--red);width:calc(100% - 10px);height:calc(100% - 10px);display:flex;flex-direction:column;align-items:center;justify-content:center;color:var(--white);font-family:"Questrial",sans-serif;line-height:1;white-space:nowrap}
.signup{left:283px;top:197px;width:133px;height:48px}
.signup .big{font-size:16px;font-weight:700}
.signup .small{font-size:6px;margin-top:2px}

.pill{border-radius:9px;background:var(--red);border:2px solid var(--pink-soft);color:var(--white);font-family:"Questrial",sans-serif;font-weight:700;text-align:center;white-space:nowrap}
.member-login{left:304px;top:266px;width:84px;height:18px;font-size:10px;line-height:14px}
.login-note{left:278px;top:289px;width:142px;text-align:center;font-size:5.5px;color:var(--ink)}
.field{border:1px solid #c9c9c9;height:13px;font-size:5.5px;color:#999;padding:3px 3px;background:#fff}
.f-user{left:278px;top:298px;width:63px}
.f-pass{left:357px;top:298px;width:63px}

.side-menu{left:276px;top:327px;width:144px}
.side-menu a{display:block;height:24px;margin-bottom:3.5px;background:var(--red);border:2px solid var(--pink-soft);color:var(--white);font-family:"Questrial",sans-serif;font-size:11px;line-height:20px;text-align:center;text-decoration:none}

.side-tab{display:flex;align-items:center;justify-content:center;color:var(--white)}
.book-tab{left:238px;top:272px;width:30px;height:128px;background:var(--red)}
.book-tab span{transform:rotate(-90deg);white-space:nowrap;font-family:"Questrial",sans-serif;font-size:12px;font-weight:700;line-height:10px;text-align:center}
.book-tab small{display:block;font-size:5px;font-weight:400}
.social-tab{left:822px;top:275px;width:30px;height:137px;background:var(--blue)}
.social-tab span{transform:rotate(-90deg);white-space:nowrap;font-family:"Questrial",sans-serif;font-size:12px}
.social-icons{left:852px;top:276px;width:32px}
.social-icons div{width:32px;height:32px;margin-bottom:3px;border-radius:4px;display:flex;align-items:center;justify-content:center;font-size:6.5px;color:var(--white);font-family:"Arimo",sans-serif}
.si-1{background:#45b0e3}.si-2{background:#f08a1d}.si-3{background:#b5b5b5}.si-4{background:#3b5b9a}

/* hero */
.hero{left:428px;top:95px;width:370px;height:175px;background:radial-gradient(ellipse at 30% 45%,#7a1020,#2a0508 55%),linear-gradient(120deg,#1a0a10,#5a5a7a);background-blend-mode:screen}
.hero-band{left:428px;top:218px;width:370px;height:50px;background:rgba(60,60,60,.55)}
.hero-caption{left:438px;top:235px;color:#f3f3f3;font-family:"Questrial",sans-serif;font-size:16px;letter-spacing:.2px;white-space:nowrap}

.intro{left:429px;top:276px;width:369px;font-size:6.3px;line-height:8.6px;color:var(--grey)}
.intro h1{font-size:9px;color:var(--ink);font-weight:700;margin-bottom:6px;line-height:12px}
.intro h2{font-size:7px;color:var(--ink);font-weight:700;margin:8px 0 6px}
.intro p{margin-bottom:8px}

.rule{height:1px;background:var(--pink)}
.book-rule{left:428px;top:473px;width:240px}
.book-oval{left:668px;top:450px;width:134px;height:50px}
.book-oval .big{font-size:15px;font-weight:700}
.book-oval .small{font-size:5.5px;margin-top:2px}

.section-tab{height:25px;display:flex;border:2px solid var(--pink);white-space:nowrap}
.section-tab span{font-family:"Questrial",sans-serif;font-weight:700;font-size:13px;line-height:21px;padding:0 5px}
.tab-news{left:428px;top:485px;width:120px}
.tab-news .a{background:var(--red);color:#fff}
.tab-news .b{background:#fff;color:var(--ink)}
.tab-exh{left:428px;top:689px;width:119px;background:var(--red)}
.tab-exh span{color:#fff}
.view-all{font-size:5.5px;color:var(--ink);font-weight:700;white-space:nowrap}

.card{width:113px}
.card .photo{height:112px;border:1px solid #333}
.card p{font-size:6.2px;line-height:7.8px;color:var(--grey);margin-top:8px}
.card p b{color:var(--ink)}
.card .more{display:block;text-align:right;font-size:5.5px;color:var(--ink);margin-top:3px}
.p-a{background:linear-gradient(160deg,#3a3a3a,#7a4a2a 50%,#1a1a1a)}
.p-b{background:linear-gradient(160deg,#9a9a9a,#4a1a1a 60%,#2a2a2a)}
.p-c{background:linear-gradient(160deg,#d8d8d8,#b8a890 50%,#6a5a4a)}
.p-d{background:linear-gradient(160deg,#cfd8e4,#3a5fa0 50%,#c84a2a)}
.p-e{background:linear-gradient(160deg,#6a6a6a,#b88a5a 50%,#3a3a3a)}
.p-f{background:linear-gradient(160deg,#9aa2a8,#e8e8e8 50%,#c8a88a)}
.news-rule{left:428px;top:680px;width:372px}

.mrec{width:172px;height:142px;background:var(--black);color:#fff;text-align:center;font-family:"Arimo",sans-serif;font-weight:700;padding-top:38px}
.mrec .size{font-size:12px;line-height:14px}
.mrec .note{font-size:9px;line-height:14px;margin-top:12px}

/* left column boxes */
.box{border:1px solid var(--blue);background:#fff}
.box-head{font-family:"Questrial",sans-serif;font-size:10px;color:var(--blue);line-height:11px}
.box-head b{color:var(--red-dark);font-weight:700}
.recipe{left:276px;top:482px;width:142px;height:183px;padding:3px}
.recipe .box-head{text-align:center;font-size:9.5px}
.recipe p,.newsletter p{font-size:5.8px;line-height:7.6px;margin-top:4px;color:var(--ink)}
.recipe .photo{height:40px;margin:5px 4px;background:linear-gradient(180deg,#7fae4a,#b8542a 60%,#e0c07a)}
.mini-fields{display:flex;justify-content:space-between;margin:6px 4px 0}
.mini-fields .field{position:static;width:60px}
.wide-field{margin:6px 4px 0}
.join-btn,.send-btn{width:68px;height:16px;margin:9px auto 0;font-size:9px;line-height:12px}

.feed{left:277px;top:676px;width:141px;height:106px;padding:3px}
.feed-head{display:flex;justify-content:space-between;align-items:center;border-bottom:1px solid #ddd;padding-bottom:4px}
.feed-head i{width:18px;height:18px;background:#45b0e3;border-radius:3px}
.feed-body{display:flex;gap:4px;margin-top:10px;align-items:center}
.feed-brand{width:58px;flex:none;font-family:"Questrial",sans-serif;font-size:9px;line-height:10px;color:#2a2a2a}
.feed-body p{font-size:5.6px;line-height:7px;color:var(--grey)}
.feed small{display:block;font-size:5.6px;margin-top:12px;margin-left:4px}
.feed small span{color:var(--blue)}

.newsletter{left:277px;top:790px;width:141px;height:135px;padding:3px}
.newsletter .box-head{text-align:center;font-size:9px;white-space:nowrap}
.newsletter p{margin:7px 2px 0}

.partners{left:278px;top:940px;width:140px;display:flex;justify-content:space-between;align-items:center}
.partner-a{width:52px;height:9px;background:#1a1a1a}
.partner-b{width:36px;height:22px;background:#555}
.partner-c{width:24px;height:24px;border-radius:50%;border:2px solid #555}
.spoons{left:277px;top:968px;width:140px;height:88px;background:linear-gradient(90deg,#d8c35a,#a8b870 25%,#e0b050 50%,#c83a2a 72%,#8a9a4a);border-radius:4px}

/* footer */
.footer{left:268px;top:1055px;width:552px;height:115px;background:var(--red)}
.org{left:294px;top:1072px;color:#fff;font-size:5.5px;line-height:8px}
.org strong{display:block;font-size:9px;color:#1a1a1a;font-family:"Arimo",sans-serif;margin-bottom:3px}
.org .terms{margin-top:16px}
.fcol{width:112px;height:96px;border:1px solid #fff;border-top:none}
.fcol h3{background:#fff;border:1px solid var(--red);font-size:7px;font-weight:700;color:var(--ink);height:15px;line-height:13px;padding-left:9px;margin:-1px -1px 0;white-space:nowrap}
.fcol ul{list-style:none;padding:9px 0 0 10px}
.fcol li{color:#fff;font-size:6px;line-height:8.2px}
.fcol-1{left:428px;top:1039px}
.fcol-2{left:557px;top:1039px}
.fcol-3{left:688px;top:1039px}
.foot-links{left:520px;top:1145px;width:282px;text-align:right;color:#fff;font-size:5.5px;white-space:nowrap}
</style>
</head>
<body>
<div class="canvas">

  <div class="skin" role="img" aria-label="Sunny sky backdrop with colourful rays, swirls, streamers and garden silhouettes"></div>
  <div class="skin-piece skin-wine" role="img" aria-label="White wine being poured from a bottle into a glass"></div>
  <div class="skin-piece skin-spoons" role="img" aria-label="Spoons of colourful spices"></div>
  <div class="skin-piece skin-board" role="img" aria-label="Wooden chopping board with chillies"></div>
  <div class="skin-piece skin-veg" role="img" aria-label="Tomato, capsicum and cucumber slices"></div>
  <div class="skin-piece skin-balloon" role="img" aria-label="Pink balloon"></div>

  <div class="page"></div>

  <div class="abs dates">
    <div><b>Melbourne &nbsp; June 1 - 3, 2012 &nbsp;|</b><b>Sydney &nbsp; June 22 -24, 2012 &nbsp;|</b><b>Perth &nbsp; July 13 - 15, 2012 &nbsp;|</b></div>
    <div><b>Adelaide &nbsp; October 12 -14, 2012 &nbsp;|</b><b>Brisbane &nbsp; November 9 - 11, 2012 &nbsp;|</b></div>
  </div>
  <div class="abs dates-rule"></div>

  <nav class="abs nav">
    <ul><li>Home</li><li>Location</li><li>Tickets</li><li>Blog</li><li>Sign Up</li><li>Exhibitors</li></ul>
  </nav>
  <div class="abs pot" role="img" aria-label="Red cooking pot with wooden spoon"></div>

  <div class="abs brand"><span class="brand-dot"></span>Bright Plate &amp; Vine Fair</div>

  <div class="abs cta-oval signup"><div class="inner"><span class="big">SIGNUP HERE</span><span class="small">To Become A Member!</span></div></div>

  <div class="abs pill member-login">Member Login</div>
  <div class="abs login-note">Already a member? Please log in here</div>
  <div class="abs field f-user">Username</div>
  <div class="abs field f-pass">Password</div>

  <div class="abs side-menu">
    <a href="#">Features</a><a href="#">Chefs</a><a href="#">Plan Your Day</a><a href="#">Want To Exhibit?</a>
  </div>

  <div class="abs side-tab book-tab"><span>BOOK TICKETS<small>for your visit today!</small></span></div>
  <div class="abs side-tab social-tab"><span>SOCIALISE WITH US</span></div>
  <div class="abs social-icons">
    <div class="si-1">Chirper</div><div class="si-2">Journalr</div><div class="si-3">Reelhub</div><div class="si-4">Friendwall</div>
  </div>

  <div class="abs hero" role="img" aria-label="Two glasses of red wine with light trails"></div>
  <div class="abs hero-band"></div>
  <div class="abs hero-caption">SUCCUMB TO YOUR SENSES</div>

  <section class="abs intro">
    <h1>WELCOME TO BRIGHT PLATE AND VINE FAIR 2012</h1>
    <p>Lorem ipsum dolor sit amet, consectetur adipisicing elit, sed do eiusmod tempor incididunt ut labore et dolore magna aliqua. Ut enim ad minim veniam, quis nostrud exercitation ullamco laboris nisi ut aliquip ex ea commodo consequat.</p>
    <p>Duis aute irure dolor in reprehenderit in voluptate velit esse cillum dolore eu fugiat nulla pariatur. Excepteur sint occaecat cupidatat non proident, sunt in culpa qui officia deserunt mollit anim id est laborum.</p>
    <p>Lorem ipsum dolor sit amet, consectetur adipisicing elit, sed do eiusmod tempor incididunt ut labore et dolore magna aliqua. Ut enim ad minim veniam, quis nostrud exercitation ullamco laboris nisi ut aliquip ex ea commodo consequat.</p>
    <h2>What is the Bright Plate &amp; Vine Fair?</h2>
    <p>Lorem ipsum dolor sit amet, consectetur adipisicing elit, sed do eiusmod tempor incididunt ut labore et dolore magna aliqua. Ut enim ad minim veniam, quis nostrud exercitation ullamco laboris nisi ut aliquip ex ea commodo consequat.</p>
    <p>Duis aute irure dolor in reprehenderit in voluptate velit esse cillum dolore eu fugiat nulla pariatur. Excepteur sint occaecat cupidatat non proident, sunt in culpa qui officia deserunt mollit anim id est laborum.</p>
  </section>

  <div class="abs rule book-rule"></div>
  <div class="abs cta-oval book-oval"><div class="inner"><span class="big">BOOK TICKETS</span><span class="small">for your visit today!</span></div></div>

  <div class="abs section-tab tab-news"><span class="a">News</span><span class="b">Highlights</span></div>
  <div class="abs view-all" style="left:555px;top:505px">View All News</div>

  <article class="abs card" style="left:428px;top:518px">
    <div class="photo p-a" role="img" aria-label="Signature dish being plated"></div>
    <p><b>Over 100 signature dishes</b> quis nostrud exercitation ullamco incididunt ut labore et dolore.</p>
    <span class="more">Read more</span>
  </article>
  <article class="abs card" style="left:557px;top:518px">
    <div class="photo p-b" role="img" aria-label="Red wine tasting glasses and bottle"></div>
    <p><b>Indulge in wine tasting</b> quis nostrud exercitation ullamco incididunt ut labore et dolore.</p>
    <span class="more">Read more</span>
  </article>
  <article class="abs card" style="left:688px;top:518px">
    <div class="photo p-c" role="img" aria-label="Chefs cooking on stage"></div>
    <p><b>Award Master Chef</b> quis nostrud exercitation ullamco incididunt ut labore et dolore.</p>
    <span class="more">Read more</span>
  </article>
  <div class="abs rule news-rule"></div>

  <div class="abs section-tab tab-exh"><span>New Exhibitors</span></div>
  <div class="abs view-all" style="left:558px;top:710px">View All Exhibitors</div>

  <article class="abs card" style="left:428px;top:723px">
    <div class="photo p-d" role="img" aria-label="Exhibitor stand with product displays"></div>
    <p><b>Exhibitors info</b> quis nostrud exercitation ullamco incididunt ut labore et dolore.</p>
    <span class="more">Read more</span>
  </article>
  <article class="abs card" style="left:557px;top:723px">
    <div class="photo p-e" role="img" aria-label="Busy exhibition hall with visitors"></div>
    <p><b>Exhibitors info</b> quis nostrud exercitation ullamco incididunt ut labore et dolore.</p>
    <span class="more">Read more</span>
  </article>
  <article class="abs card" style="left:688px;top:723px">
    <div class="photo p-f" role="img" aria-label="Exhibitor offering food samples"></div>
    <p><b>Exhibitors info</b> quis nostrud exercitation ullamco incididunt ut labore et dolore.</p>
    <span class="more">Read more</span>
  </article>

  <div class="abs mrec" style="left:429px;top:883px"><div class="size">MREC Size<br>300 x 250</div><div class="note">Ad space for<br>Exhibitors &amp; Sponsors</div></div>
  <div class="abs mrec" style="left:630px;top:885px"><div class="size">MREC Size<br>300 x 250</div><div class="note">Ad space for<br>Exhibitors &amp; Sponsors</div></div>

  <aside class="abs box recipe">
    <div class="box-head"><b>JOIN</b> Our Bright Plate &amp; Vine<br><b>RECIPE CLUB!</b></div>
    <p>If you want to also have access over 70 celebrity chef recipes - all for FREE - then make sure you also join our online Bright Plate &amp; Vine Recipe Club!</p>
    <div class="photo" role="img" aria-label="Grilled meat with salad"></div>
    <div class="mini-fields"><div class="field">Your name</div><div class="field">Your Surname</div></div>
    <div class="field wide-field">email address</div>
    <div class="pill join-btn">JOIN</div>
  </aside>

  <aside class="abs box feed">
    <div class="feed-head"><span class="box-head"><b>Chirper</b> Feed</span><i></i></div>
    <div class="feed-body">
      <div class="feed-brand">Bright Plate &amp; Vine Fair</div>
      <p>Lorem ipsum dolor sit magna aliqua. Ut eni modo consequat.</p>
    </div>
    <small>Follow us on <span>Chirper</span></small>
  </aside>

  <aside class="abs box newsletter">
    <div class="box-head"><b>SIGN UP</b> To Receive Our <b>FREE</b><br>e-Newsletter</div>
    <p>Register to receive our e-newsletter on show updates, exclusive offers and the latest news.</p>
    <div class="mini-fields"><div class="field">Your name</div><div class="field">Your Surname</div></div>
    <div class="field wide-field">email address</div>
    <div class="pill send-btn">SIGN UP</div>
  </aside>

  <div class="abs partners">
    <div class="partner-a" role="img" aria-label="Partner badge"></div>
    <div class="partner-b" role="img" aria-label="Partner badge"></div>
    <div class="partner-c" role="img" aria-label="Partner badge"></div>
  </div>
  <div class="abs spoons" role="img" aria-label="Row of spoons holding coloured spices"></div>

  <footer class="abs footer"></footer>
  <div class="abs org">
    <strong>Meridian</strong>
    Event organised by<br>Meridian Events Australia © 2007
    <div class="terms">Competition Terms &amp; Conditions</div>
  </div>
  <div class="abs fcol fcol-1"><h3>Bright Plate &amp; Vine Fair</h3><ul><li>Home</li><li>Location</li><li>Tickets</li><li>Blog</li><li>Sign Up</li><li>Exhibitors</li></ul></div>
  <div class="abs fcol fcol-2"><h3>Features</h3><ul><li>Celebrity Theatre</li><li>Cheese Masterclass</li><li>Cooking School</li><li>Decanter Bar</li><li>Restaurant</li><li>Wine Theatre</li><li>Exhibitor list</li><li>Floor plans</li></ul></div>
  <div class="abs fcol fcol-3"><h3>Chef Bio's</h3><ul><li>Lena Marsh</li><li>Tom Harlow</li><li>Nico Varellas</li><li>Luc Bernard</li><li>Sam Keating</li><li>Reed Carver</li><li>Recipe Club</li><li>Login</li></ul></div>
  <div class="abs foot-links">contact us &nbsp;|&nbsp; general information &nbsp;|&nbsp; news &amp; media releases &nbsp;|&nbsp; sponsors &nbsp;|&nbsp; exhibitor information</div>

</div>
</body>
</html>
```